Lanternfield Systems Bi Fold Brocher

I need a bi fold (front/back page 1 & front/back page 2) color brochure designed to pass out to clients at a convention. My website is lanternfieldsys.example. Please take images and text from the website to create the brochure. Use the products and product descriptions to display what we offer. Use the text and quotes to describe what we do. Make it professional, descriptive, and full of useful information.

Industry/Entity Type

Business Software

Font styles to use
Serif

Colors
00a990
33b8a4
86cfc6
fbf289
0255a3
3377b5
85acd3

Requirements
Must have
• Contact Info:
• Address:
• 728 Mossgate Boulevard
• Building 200, Suite 1187
• Cumming, GA 30987
• Telephone: 1 (555) 274.8816
• Toll Free: 1 (800) 555.0147
• Email: contact@lanternfieldsys.example
Nice to have
• Good backrounds

```html
<!DOCTYPE html>
<html lang="en">
<head>
<meta charset="utf-8">
<title>Lanternfield Systems — Bi-fold Brochure</title>
<link href="https://fonts.googleapis.com/css2?family=Arimo:wght@400;700&display=swap" rel="stylesheet">
<style>
  :root {
    --teal: #0e786c;
    --teal-tick: #1fa88f;
    --navy: #0f3252;
    --white: #ffffff;
    --ink: #111111;
    --contact-ink: #173a5c;
  }
  * { box-sizing: border-box; margin: 0; padding: 0; }
  html, body { width: 1200px; height: 848px; overflow: hidden; background: var(--white); }
  body { font-family: "Arimo", Arial, sans-serif; position: relative; }

  .block { position: absolute; }

  .headline-panel { left: 0; top: 0; width: 597px; height: 172px; background: var(--teal); }
  .headline-panel h2 {
    position: absolute; left: 74px; top: 76px;
    color: var(--white); font-weight: 400; font-size: 34px; line-height: 36px; letter-spacing: -0.5px;
  }

  .brand-panel { left: 597px; top: 0; width: 595px; height: 172px; background: var(--navy); }
  .brand-name {
    position: absolute; left: 110px; top: 62px;
    display: flex; align-items: center; gap: 14px;
    color: var(--white); font-weight: 700; font-size: 40px; letter-spacing: -0.5px;
  }
  .brand-name .dot { width: 34px; height: 34px; border-radius: 50%; background: var(--white); }

  .benefits-panel {
    left: 0; top: 180px; width: 331px; height: 260px;
    background: linear-gradient(180deg, #f4f6f6 0%, #e9ecea 55%, #dfe1dc 100%);
  }
  .benefits { position: absolute; left: 76px; top: 8px; list-style: none; }
  .benefits li {
    display: flex; align-items: center; gap: 4px;
    font-size: 12.5px; color: var(--ink); height: 25.6px; letter-spacing: -0.2px;
  }
  .benefits svg { width: 9px; height: 9px; flex: none; }

  .photo-container { left: 331px; top: 180px; width: 264px; height: 260px;
    background: linear-gradient(160deg, #8fc3cf 0%, #2f8ea3 40%, #1f6f80 75%, #4a4a42 100%); }
  .photo-locomotive { left: 595px; top: 180px; width: 597px; height: 260px;
    background: linear-gradient(90deg, #a9b6bd 0%, #c9cccb 30%, #8a6a5a 55%, #c6c4c0 75%, #b8b3ad 100%); }

  .link-band { left: 0; top: 447px; width: 1192px; height: 81px; background: var(--navy); }
  .site-link {
    position: absolute; top: 31px; display: flex; align-items: center; gap: 3px;
    color: var(--white); font-weight: 700; font-size: 16.5px;
  }
  .site-link svg { width: 18px; height: 18px; }
  .site-link.left { left: 75px; }
  .site-link.right { left: 944px; }

  .contact-panel { left: 0; top: 537px; width: 595px; height: 305px; background: var(--white); }
  .contact-brand {
    position: absolute; left: 74px; top: 112px;
    display: flex; align-items: center; gap: 8px;
    color: var(--navy); font-weight: 700; font-size: 20px;
  }
  .contact-brand .dot { width: 18px; height: 18px; border-radius: 50%; background: var(--navy); }
  .contact { position: absolute; left: 331px; top: 112px; color: var(--contact-ink); font-size: 11px; line-height: 13.5px; }
  .contact h3 { font-weight: 400; font-size: 16px; margin-bottom: 4px; }
  .contact p + p { margin-top: 6px; }

  .cover-panel { left: 595px; top: 537px; width: 597px; height: 305px; background: var(--teal); }
  .cover-panel h1 {
    position: absolute; left: 174px; top: 52px;
    color: var(--white); font-weight: 700; font-size: 40px; line-height: 56px; letter-spacing: -0.3px;
  }
</style>
</head>
<body>
  <section class="block headline-panel">
    <h2>Cost Savings &amp;<br>Efficiencies</h2>
  </section>

  <section class="block brand-panel">
    <div class="brand-name"><span class="dot"></span>Lanternfield Systems</div>
  </section>

  <section class="block benefits-panel" role="img" aria-label="Faded photo of a rail yard with freight cars">
    <ul class="benefits">
      <li><svg viewBox="0 0 10 10"><path d="M1 5.5 L4 8.5 L9 1.5" fill="none" stroke="var(--teal-tick)" stroke-width="2"/></svg>Improved Yard Control</li>
      <li><svg viewBox="0 0 10 10"><path d="M1 5.5 L4 8.5 L9 1.5" fill="none" stroke="var(--teal-tick)" stroke-width="2"/></svg>Corporate Analytics and Dashboards</li>
      <li><svg viewBox="0 0 10 10"><path d="M1 5.5 L4 8.5 L9 1.5" fill="none" stroke="var(--teal-tick)" stroke-width="2"/></svg>Railcar Inspections</li>
      <li><svg viewBox="0 0 10 10"><path d="M1 5.5 L4 8.5 L9 1.5" fill="none" stroke="var(--teal-tick)" stroke-width="2"/></svg>Maintain Railcar Statuses</li>
      <li><svg viewBox="0 0 10 10"><path d="M1 5.5 L4 8.5 L9 1.5" fill="none" stroke="var(--teal-tick)" stroke-width="2"/></svg>Reduction in Human Error</li>
      <li><svg viewBox="0 0 10 10"><path d="M1 5.5 L4 8.5 L9 1.5" fill="none" stroke="var(--teal-tick)" stroke-width="2"/></svg>Demurrage Management</li>
      <li><svg viewBox="0 0 10 10"><path d="M1 5.5 L4 8.5 L9 1.5" fill="none" stroke="var(--teal-tick)" stroke-width="2"/></svg>Customer Portals</li>
      <li><svg viewBox="0 0 10 10"><path d="M1 5.5 L4 8.5 L9 1.5" fill="none" stroke="var(--teal-tick)" stroke-width="2"/></svg>Functionality</li>
      <li><svg viewBox="0 0 10 10"><path d="M1 5.5 L4 8.5 L9 1.5" fill="none" stroke="var(--teal-tick)" stroke-width="2"/></svg>Organization</li>
      <li><svg viewBox="0 0 10 10"><path d="M1 5.5 L4 8.5 L9 1.5" fill="none" stroke="var(--teal-tick)" stroke-width="2"/></svg>Automation</li>
    </ul>
  </section>

  <div class="block photo-container" role="img" aria-label="Photo of a blue shipping container on a rail flatcar"></div>
  <div class="block photo-locomotive" role="img" aria-label="Photo of a switching locomotive pulling loaded flatcars"></div>

  <section class="block link-band">
    <div class="site-link left"><svg viewBox="0 0 18 18"><circle cx="9" cy="9" r="9" fill="var(--teal-tick)"/><path d="M6 5 L12 9 L6 13" fill="none" stroke="var(--white)" stroke-width="2"/></svg>lanternfieldsys.example</div>
    <div class="site-link right"><svg viewBox="0 0 18 18"><circle cx="9" cy="9" r="9" fill="var(--teal-tick)"/><path d="M6 5 L12 9 L6 13" fill="none" stroke="var(--white)" stroke-width="2"/></svg>lanternfieldsys.example</div>
  </section>

  <section class="block contact-panel">
    <div class="contact-brand"><span class="dot"></span>Lanternfield Systems</div>
    <div class="contact">
      <h3>Contact Info:</h3>
      <p>728 Mossgate Boulevard<br>Building 200, Suite 1187<br>Cumming, GA 30987</p>
      <p>Telephone: 1 (555) 274.8816<br>Toll Free: 1 (800) 555.0147</p>
      <p>Email: contact@lanternfieldsys.example</p>
    </div>
  </section>

  <section class="block cover-panel">
    <h1>Rail terminal<br>management<br>Software</h1>
  </section>
</body>
</html>
```